Business Card Design Project

I am a Chiropractor that is looking for a new business card.  Our logo was slightly changed lately, therefore need a new, more professional look.
We are a modern, non-stuffy chiropractic office.  Want a contemporary look that will let people know this is not your typical doctors office.  Our logo is red, and contains the name of our business: realign.  The u in the logo is green, stressing the most important part of our business: "u"

Target Market(s)
moderate to upper income bracket, family friendly
www.realignspine-example.com
Gordon Pell
Family Chiropractor
314 Hollis Rd
Corrow Falls, TX 78999
512.555.0147 phone
512.555.0148 fax
Industry/Entity Type
Business
Requirements
Must have
- www.realignspine-example.com
Gordon Pell
Family Chiropractor
314 Hollis Rd
Corrow Falls, TX 78999
512.555.0147 phone
512.555.0148 fax

```html
<!DOCTYPE html>
<html lang="en">
<head>
<meta charset="utf-8">
<title>realign – Business Card</title>
<link rel="stylesheet" href="https://fonts.googleapis.com/css2?family=Didact+Gothic&display=swap">
<style>
  :root {
    --backdrop: #c4c4c4;
    --card: #f1f1f1;
    --ink: #1a1a1a;
    --brand-red: #e8140a;
    --brand-red-dark: #d20f06;
    --paper-white: #ffffff;
    --rule: #3a3a3a;
    --rule-shadow: rgba(0, 0, 0, 0.10);
  }
  * { margin: 0; padding: 0; box-sizing: border-box; }
  html, body {
    width: 1200px;
    height: 682px;
    overflow: hidden;
  }
  body {
    position: relative;
    background: var(--backdrop);
    font-family: "Didact Gothic", "Century Gothic", sans-serif;
    color: var(--ink);
  }
  .card {
    position: absolute;
    top: 192px;
    width: 498px;
    height: 299px;
    background: var(--card);
    border-radius: 5px;
    overflow: hidden;
  }
  .card--front { left: 68px; }
  .card--back { left: 628px; }

  .divider {
    position: absolute;
    height: 2px;
    background: linear-gradient(to right, transparent, var(--rule) 20%, var(--rule) 80%, transparent);
  }
  .divider::after {
    content: "";
    position: absolute;
    top: 2px;
    left: 10%;
    width: 80%;
    height: 14px;
    background: radial-gradient(ellipse at top, var(--rule-shadow), transparent 70%);
  }

  /* Front */
  .holder {
    position: absolute;
    top: 70px;
    left: 0;
    width: 100%;
    text-align: center;
  }
  .holder__name {
    font-size: 36px;
    font-weight: 400;
    line-height: 1;
    letter-spacing: 0.5px;
  }
  .holder__title {
    margin-top: 11px;
    font-size: 13.5px;
    line-height: 1;
  }
  .card--front .divider {
    top: 143px;
    left: 20px;
    width: 458px;
  }
  .contact-band {
    position: absolute;
    top: 144px;
    left: 128px;
    width: 240px;
    height: 155px;
    background: linear-gradient(to bottom, var(--brand-red-dark), var(--brand-red) 30%);
    color: var(--paper-white);
    text-align: center;
    padding-top: 30px;
    font-style: normal;
  }
  .contact-band p { line-height: 1; white-space: nowrap; }
  .contact-band .line-phone,
  .contact-band .line-fax {
    font-size: 14px;
    margin-bottom: 8px;
  }
  .contact-band .line-address {
    font-size: 16px;
    margin-bottom: 8px;
  }
  .contact-band .line-web {
    font-size: 15px;
  }

  /* Back */
  .brand-name {
    position: absolute;
    top: 114px;
    left: 0;
    width: 100%;
    text-align: center;
    font-size: 58px;
    line-height: 1;
    color: var(--brand-red);
    letter-spacing: 1px;
  }
  .card--back .divider {
    top: 239px;
    left: 20px;
    width: 458px;
  }
</style>
</head>
<body>
  <section class="card card--front" aria-label="Card front">
    <header class="holder">
      <h1 class="holder__name">Gordon Pell</h1>
      <p class="holder__title">Family Chiropractor</p>
    </header>
    <div class="divider"></div>
    <address class="contact-band">
      <p class="line-phone">Phone:. 512.555.0147</p>
      <p class="line-fax">Fax:. 512.555.0148</p>
      <p class="line-address">314 Hollis Rd</p>
      <p class="line-address">Corrow Falls, TX 78999</p>
      <p class="line-web">www.realignspine-example.com</p>
    </address>
  </section>

  <section class="card card--back" aria-label="Card back">
    <p class="brand-name">realign</p>
    <div class="divider"></div>
  </section>
</body>
</html>
```